BOLD & MINIMALIST DESIGN NEEDED

We want a very bold but minimalistic business card design that is impactful and utilizes both sides of the business card. Our current logo is included for your use.

We want bold fonts and good use of negative space. We don't want the logo to overpower the design.

Target Market(s)

Professionals who are building new commercial buildings.

Industry/Entity Type

Construction

Contact Information for Business Card

Name, Title, email, office phone, cell phone, website

Font styles to use
Serif
Sans Serif

Requirements
Must have
• Bold design!

```html
<!DOCTYPE html>
<html lang="en">
<head>
<meta charset="utf-8">
<title>Ridgecrest Design + Build — Business Card</title>
<link rel="stylesheet" href="https://fonts.googleapis.com/css2?family=Open+Sans:wght@400;600;700;800&display=swap">
<style>
  :root {
    --stage: #9b9b9b;
    --card: #f4f4f2;
    --ink: #242424;
    --ink-soft: #3a3a3a;
    --green: #8bc34a;
    --green-deep: #7ab53a;
  }
  * { box-sizing: border-box; margin: 0; padding: 0; }
  html, body {
    width: 1200px; height: 1019px; overflow: hidden;
    background: var(--stage);
    font-family: "Open Sans", Arial, sans-serif;
    color: var(--ink);
  }
  .stage {
    width: 1200px; height: 1019px;
    display: flex; flex-direction: column;
    align-items: center; justify-content: center; gap: 50px;
  }
  .card {
    position: relative;
    width: 700px; height: 400px;
    background: var(--card);
    border-radius: 34px;
    box-shadow: 0 10px 30px rgba(0,0,0,.22);
    overflow: hidden;
  }

  /* Brand side */
  .brand-band {
    position: absolute; left: 0; right: 0; top: 262px; height: 58px;
    background: var(--green);
    display: flex; align-items: center; justify-content: center;
  }
  .website {
    font-size: 24px; font-weight: 600; letter-spacing: 6px;
    color: var(--ink-soft);
  }
  .wordmark {
    position: absolute; left: 0; right: 0; top: 120px;
    display: flex; flex-direction: column; align-items: center;
  }
  .wordmark-row { display: flex; align-items: center; gap: 14px; }
  .wordmark-mark { width: 30px; height: 30px; background: var(--green); }
  .wordmark-name {
    font-size: 46px; font-weight: 800; letter-spacing: 1px; color: var(--ink);
  }
  .wordmark-tag {
    margin-top: 4px; padding-top: 4px;
    border-top: 2px solid var(--ink);
    font-size: 15px; font-weight: 400; letter-spacing: 9px; color: var(--ink-soft);
  }

  /* Contact side */
  .corner-block {
    position: absolute; left: 0; top: 22px; width: 52px; height: 52px;
    background: var(--green);
  }
  .identity { position: absolute; left: 66px; top: 22px; }
  .person-name {
    font-size: 32px; font-weight: 800; letter-spacing: -.5px;
    text-transform: uppercase; line-height: 1.05; color: var(--ink);
  }
  .person-title { font-size: 24px; font-weight: 400; color: var(--ink-soft); }
  .side-mark {
    position: absolute; right: 52px; top: 176px;
    display: flex; align-items: center; gap: 10px;
  }
  .side-mark-square { width: 18px; height: 18px; background: var(--green); }
  .side-mark-name { font-size: 26px; font-weight: 800; color: var(--ink); }
  .contacts {
    position: absolute; right: 38px; bottom: 36px;
    list-style: none; text-align: right;
  }
  .contacts li {
    display: flex; align-items: center; justify-content: flex-end; gap: 12px;
    font-size: 19px; font-weight: 600; line-height: 1.5; color: var(--ink);
  }
  .contacts svg { width: 20px; height: 20px; fill: var(--green-deep); flex: none; }
</style>
</head>
<body>
<main class="stage">

  <section class="card card-contact" aria-label="Contact side">
    <div class="corner-block"></div>
    <div class="identity">
      <h1 class="person-name">Marcus Hale</h1>
      <p class="person-title">Manager</p>
    </div>
    <div class="side-mark">
      <span class="side-mark-square"></span>
      <span class="side-mark-name">RIDGECREST</span>
    </div>
    <ul class="contacts">
      <li>021-555-0184
        <svg viewBox="0 0 24 24" aria-hidden="true"><path d="M6.6 10.8a15.1 15.1 0 0 0 6.6 6.6l2.2-2.2c.3-.3.7-.4 1-.2 1.1.4 2.3.6 3.6.6.6 0 1 .4 1 1V20c0 .6-.4 1-1 1C10.6 21 3 13.4 3 4c0-.6.4-1 1-1h3.5c.6 0 1 .4 1 1 0 1.3.2 2.5.6 3.6.1.3 0 .7-.2 1z"/></svg>
      </li>
      <li>+5550 1234 678
        <svg viewBox="0 0 24 24" aria-hidden="true"><path d="M4 4h5v16H4zM11 6h9v14h-9zM13 8v3h5V8zm0 5v2h2v-2zm3 0v2h2v-2zm-3 3v2h2v-2zm3 0v2h2v-2z"/></svg>
      </li>
      <li>hello@ridgecrestbuild.com
        <svg viewBox="0 0 24 24" aria-hidden="true"><path d="M3 5h18v14H3zm2 2v.5l7 5 7-5V7l-7 5z"/></svg>
      </li>
    </ul>
  </section>

  <section class="card card-brand" aria-label="Brand side">
    <div class="wordmark">
      <div class="wordmark-row">
        <span class="wordmark-mark"></span>
        <span class="wordmark-name">RIDGECREST</span>
      </div>
      <span class="wordmark-tag">DESIGN + BUILD</span>
    </div>
    <div class="brand-band">
      <span class="website">www.ridgecrestbuild.com</span>
    </div>
  </section>

</main>
</body>
</html>
```